Poster for a vegan café with a funny message about the food served.

Design a poster with the text "Eating here was a big missed stake!" for a café at a meditation center (lunavardet.se).

```html
<!DOCTYPE html>
<html lang="en">
<head>
<meta charset="UTF-8">
<title>Big Missed Stake – Café Poster</title>
<link rel="stylesheet" href="https://fonts.googleapis.com/css2?family=Kaushan+Script&family=Montserrat:wght@700&family=Oswald:wght@500&display=swap">
<style>
  :root {
    --backdrop: #7d5b4b;
    --paper-top: #e4e4e3;
    --paper-mid: #f2f2f1;
    --paper-low: #e9e9e8;
    --ink: #3d2a1f;
    --ink-rule: #4a3427;
    --label-text: #ffffff;
    --bean-dark: #3a2316;
    --bean-mid: #6b4430;
  }
  html, body {
    margin: 0;
    padding: 0;
    width: 1200px;
    height: 1000px;
    overflow: hidden;
    background: var(--backdrop);
  }
  .poster {
    position: absolute;
    left: 350px;
    top: 145px;
    width: 502px;
    height: 713px;
    overflow: hidden;
    background: linear-gradient(180deg, var(--paper-top) 0%, var(--paper-mid) 55%, var(--paper-low) 100%);
  }
  .poster__photo {
    position: absolute;
    left: 0;
    right: 0;
    bottom: 0;
    height: 270px;
    background:
      radial-gradient(ellipse 55% 45% at 22% 88%, var(--bean-mid) 0%, var(--bean-dark) 55%, transparent 80%),
      radial-gradient(ellipse 60% 25% at 72% 98%, var(--bean-mid) 0%, var(--bean-dark) 55%, transparent 85%),
      linear-gradient(180deg, transparent 0%, rgba(200,200,198,0.35) 60%, rgba(120,90,70,0.25) 100%);
  }
  .headline {
    position: absolute;
    left: 0;
    top: 0;
    width: 100%;
    margin: 0;
    color: var(--ink);
    font-weight: normal;
  }
  .headline__script {
    position: absolute;
    left: 0;
    width: 100%;
    text-align: center;
    font-family: "Kaushan Script", cursive;
    line-height: 1;
  }
  .headline__opening {
    top: 160px;
    font-size: 70px;
  }
  .headline__connector {
    position: absolute;
    top: 250px;
    left: 62px;
    width: 370px;
    display: flex;
    align-items: center;
    gap: 18px;
    font-family: "Montserrat", sans-serif;
    font-weight: 700;
    font-size: 34px;
    line-height: 1;
  }
  .headline__rule {
    flex: 1;
    height: 2px;
    background: var(--ink-rule);
  }
  .headline__emphasis {
    position: absolute;
    top: 298px;
    left: 76px;
    display: flex;
    align-items: center;
    gap: 22px;
    font-family: "Oswald", sans-serif;
    font-weight: 500;
    font-size: 50px;
    line-height: 1;
    letter-spacing: 6px;
  }
  .headline__label {
    display: inline-block;
    padding: 4px 10px 6px 12px;
    border-radius: 8px;
    background: var(--ink);
    color: var(--label-text);
    letter-spacing: 5px;
  }
  .headline__punchline {
    top: 370px;
    font-size: 140px;
  }
</style>
</head>
<body>
  <main class="poster">
    <div class="poster__photo" role="img" aria-label="Photo of roasted coffee beans spilling from a tipped-over glass jar"></div>
    <h1 class="headline">
      <span class="headline__script headline__opening">Eating here</span>
      <span class="headline__connector"><span class="headline__rule"></span>was a<span class="headline__rule"></span></span>
      <span class="headline__emphasis"><span class="headline__label">BIG</span>MISSED</span>
      <span class="headline__script headline__punchline">stake!</span>
    </h1>
  </main>
</body>
</html>
```